Kestrel Ink BC 2019

Hi!
As seen from the attached, I created a 2018 BC that I really like.
It features company details on one side, and a calendar on the other side. The BC is 7" x 2" with a score, so folded it's a regular sized BC.
Company details remain the same, but I need to upgrade and refresh the calendar to 2019. Let your creative juices flow!

The submitted designs so far, while not terrible, most don't take into account that I need a refresher on the current design, but it's a BC that is double sided, and the size of a BC that's side by side wide, with score. (see the attached BC 2018 design). I need the BC to be updated with a 2019 calendar, but essentially because it's such a tiny size, to work the realistic space allocated, and make it readable and striking to stand out and very usable/practical. Let's do this people!

```html
<!DOCTYPE html>
<html lang="en">
<head>
<meta charset="utf-8">
<title>Kestrel Ink – Business Card 2019</title>
<link rel="stylesheet" href="https://fonts.googleapis.com/css2?family=Quicksand:wght@400;500&family=Roboto+Condensed:wght@400;700&display=swap">
<style>
  :root {
    --backdrop: #e2e2e2;
    --card: #2f2d2d;
    --ink-white: #f4f4f4;
    --ink-soft: #d9d9d9;
    --weekend: #f2ec2a;
    --weekend-ink: #2f2d2d;
  }
  * { margin: 0; padding: 0; box-sizing: border-box; }
  html, body {
    width: 1200px;
    height: 900px;
    overflow: hidden;
    background: var(--backdrop);
  }
  .canvas {
    position: relative;
    width: 1200px;
    height: 900px;
  }
  .card {
    position: absolute;
    left: 250px;
    width: 700px;
    height: 400px;
    background: var(--card);
    border-radius: 3px;
    color: var(--ink-white);
  }
  .card-front { top: 35px; font-family: "Quicksand", sans-serif; }
  .card-back { top: 465px; font-family: "Roboto Condensed", sans-serif; }

  /* Front face */
  .brand {
    position: absolute;
    left: 90px;
    top: 180px;
    display: flex;
    align-items: center;
    gap: 14px;
  }
  .brand-square {
    width: 28px;
    height: 28px;
    background: var(--ink-white);
  }
  .brand-name {
    font-size: 38px;
    font-weight: 500;
    letter-spacing: 1px;
    line-height: 1;
  }
  .contact-lines {
    position: absolute;
    right: 58px;
    top: 48px;
    list-style: none;
  }
  .contact-lines li {
    display: flex;
    align-items: center;
    justify-content: flex-end;
    gap: 18px;
    font-size: 21px;
    letter-spacing: 1.2px;
    height: 37px;
  }
  .contact-icon {
    width: 25px;
    height: 22px;
    fill: var(--ink-white);
  }
  .web-lines {
    position: absolute;
    right: 58px;
    top: 250px;
    text-align: right;
    font-size: 19px;
    letter-spacing: 0.8px;
    line-height: 37px;
  }

  /* Calendar face */
  .calendar {
    position: absolute;
    inset: 16px 24px;
    display: grid;
    grid-template-columns: repeat(4, 1fr);
    grid-template-rows: repeat(3, 1fr);
    column-gap: 12px;
    row-gap: 4px;
  }
  .month {
    display: flex;
    flex-direction: column;
    align-items: center;
  }
  .weekdays,
  .days {
    display: grid;
    grid-template-columns: repeat(7, 22px);
    text-align: center;
  }
  .weekdays {
    font-size: 8px;
    font-weight: 700;
    line-height: 12px;
    color: var(--ink-soft);
    margin-bottom: 1px;
  }
  .weekdays .weekend {
    background: var(--weekend);
    color: var(--weekend-ink);
  }
  .days {
    font-size: 10px;
    line-height: 12px;
    color: var(--ink-white);
  }
  .days i { font-style: normal; }
  .days i:first-child { grid-column-start: var(--start); }
  .month-name {
    margin-top: 3px;
    font-size: 12px;
    font-weight: 700;
    letter-spacing: 0.5px;
    color: var(--ink-soft);
  }
  .year {
    font-size: 13px;
    font-weight: 700;
    color: var(--ink-soft);
    line-height: 1;
  }
</style>
</head>
<body>
<main class="canvas">
  <section class="card card-front">
    <div class="brand">
      <span class="brand-square"></span>
      <span class="brand-name">Kestrel Ink</span>
    </div>

    <ul class="contact-lines">
      <li>
        <svg class="contact-icon" viewBox="0 0 30 26" aria-hidden="true">
          <path d="M8 2c1-1 2.5-1 3.2.2l2.2 3.6c.6 1 .3 2.2-.6 2.8l-1.6 1.1c1.3 2.8 3.3 4.9 6 6.2l1.1-1.6c.6-.9 1.8-1.2 2.8-.6l3.6 2.2c1.2.7 1.2 2.2.2 3.2l-1.6 1.6C21 24 17 23 12.6 18.6S6 10 8.3 6.4z"/>
        </svg>
        <span>555.210.4816</span>
      </li>
      <li>
        <svg class="contact-icon" viewBox="0 0 30 26" aria-hidden="true">
          <ellipse cx="12" cy="10" rx="11" ry="8"/>
          <path d="M5 16l-3 6 8-4z"/>
          <ellipse cx="20" cy="15" rx="9" ry="6.5" fill="#2f2d2d"/>
          <ellipse cx="20" cy="15" rx="8" ry="5.5"/>
          <path d="M25 19l3 5-7-3z"/>
        </svg>
        <span>555.318.2064</span>
      </li>
      <li>
        <svg class="contact-icon" viewBox="0 0 30 26" aria-hidden="true">
          <path d="M11 3h8a2 2 0 0 1 2 2v2h-2V5h-8v2H9V5a2 2 0 0 1 2-2z"/>
          <rect x="1" y="8" width="28" height="16" rx="2"/>
          <rect x="13" y="13" width="4" height="4" fill="#2f2d2d"/>
        </svg>
        <span>555.210.4817</span>
      </li>
    </ul>

    <div class="web-lines">
      <p>pickup@kestrelink.com</p>
      <p>kestrelink.com</p>
    </div>
  </section>

  <section class="card card-back" aria-label="2019 calendar">
    <div class="calendar">
      <div class="month">
        <div class="weekdays"><span>SUN</span><span>MON</span><span>TUE</span><span>WED</span><span>THU</span><span class="weekend">FRI</span><span class="weekend">SAT</span></div>
        <div class="days" style="--start:3"><i>1</i><i>2</i><i>3</i><i>4</i><i>5</i><i>6</i><i>7</i><i>8</i><i>9</i><i>10</i><i>11</i><i>12</i><i>13</i><i>14</i><i>15</i><i>16</i><i>17</i><i>18</i><i>19</i><i>20</i><i>21</i><i>22</i><i>23</i><i>24</i><i>25</i><i>26</i><i>27</i><i>28</i><i>29</i><i>30</i><i>31</i></div>
        <p class="month-name">JAN</p>
      </div>
      <div class="month">
        <div class="weekdays"><span>SUN</span><span>MON</span><span>TUE</span><span>WED</span><span>THU</span><span class="weekend">FRI</span><span class="weekend">SAT</span></div>
        <div class="days" style="--start:6"><i>1</i><i>2</i><i>3</i><i>4</i><i>5</i><i>6</i><i>7</i><i>8</i><i>9</i><i>10</i><i>11</i><i>12</i><i>13</i><i>14</i><i>15</i><i>16</i><i>17</i><i>18</i><i>19</i><i>20</i><i>21</i><i>22</i><i>23</i><i>24</i><i>25</i><i>26</i><i>27</i><i>28</i></div>
        <p class="month-name">FEB</p>
      </div>
      <div class="month">
        <div class="weekdays"><span>SUN</span><span>MON</span><span>TUE</span><span>WED</span><span>THU</span><span class="weekend">FRI</span><span class="weekend">SAT</span></div>
        <div class="days" style="--start:6"><i>1</i><i>2</i><i>3</i><i>4</i><i>5</i><i>6</i><i>7</i><i>8</i><i>9</i><i>10</i><i>11</i><i>12</i><i>13</i><i>14</i><i>15</i><i>16</i><i>17</i><i>18</i><i>19</i><i>20</i><i>21</i><i>22</i><i>23</i><i>24</i><i>25</i><i>26</i><i>27</i><i>28</i><i>29</i><i>30</i><i>31</i></div>
        <p class="month-name">MAR</p>
      </div>
      <div class="month">
        <div class="weekdays"><span>SUN</span><span>MON</span><span>TUE</span><span>WED</span><span>THU</span><span class="weekend">FRI</span><span class="weekend">SAT</span></div>
        <div class="days" style="--start:2"><i>1</i><i>2</i><i>3</i><i>4</i><i>5</i><i>6</i><i>7</i><i>8</i><i>9</i><i>10</i><i>11</i><i>12</i><i>13</i><i>14</i><i>15</i><i>16</i><i>17</i><i>18</i><i>19</i><i>20</i><i>21</i><i>22</i><i>23</i><i>24</i><i>25</i><i>26</i><i>27</i><i>28</i><i>29</i><i>30</i></div>
        <p class="month-name">APR</p>
      </div>
      <div class="month">
        <div class="weekdays"><span>SUN</span><span>MON</span><span>TUE</span><span>WED</span><span>THU</span><span class="weekend">FRI</span><span class="weekend">SAT</span></div>
        <div class="days" style="--start:4"><i>1</i><i>2</i><i>3</i><i>4</i><i>5</i><i>6</i><i>7</i><i>8</i><i>9</i><i>10</i><i>11</i><i>12</i><i>13</i><i>14</i><i>15</i><i>16</i><i>17</i><i>18</i><i>19</i><i>20</i><i>21</i><i>22</i><i>23</i><i>24</i><i>25</i><i>26</i><i>27</i><i>28</i><i>29</i><i>30</i><i>31</i></div>
        <p class="month-name">MAY</p>
      </div>
      <div class="month">
        <div class="weekdays"><span>SUN</span><span>MON</span><span>TUE</span><span>WED</span><span>THU</span><span class="weekend">FRI</span><span class="weekend">SAT</span></div>
        <div class="days" style="--start:7"><i>1</i><i>2</i><i>3</i><i>4</i><i>5</i><i>6</i><i>7</i><i>8</i><i>9</i><i>10</i><i>11</i><i>12</i><i>13</i><i>14</i><i>15</i><i>16</i><i>17</i><i>18</i><i>19</i><i>20</i><i>21</i><i>22</i><i>23</i><i>24</i><i>25</i><i>26</i><i>27</i><i>28</i><i>29</i><i>30</i></div>
        <p class="month-name">JUN</p>
      </div>
      <div class="month">
        <div class="weekdays"><span>SUN</span><span>MON</span><span>TUE</span><span>WED</span><span>THU</span><span class="weekend">FRI</span><span class="weekend">SAT</span></div>
        <div class="days" style="--start:2"><i>1</i><i>2</i><i>3</i><i>4</i><i>5</i><i>6</i><i>7</i><i>8</i><i>9</i><i>10</i><i>11</i><i>12</i><i>13</i><i>14</i><i>15</i><i>16</i><i>17</i><i>18</i><i>19</i><i>20</i><i>21</i><i>22</i><i>23</i><i>24</i><i>25</i><i>26</i><i>27</i><i>28</i><i>29</i><i>30</i><i>31</i></div>
        <p class="month-name">JUL</p>
      </div>
      <div class="month">
        <div class="weekdays"><span>SUN</span><span>MON</span><span>TUE</span><span>WED</span><span>THU</span><span class="weekend">FRI</span><span class="weekend">SAT</span></div>
        <div class="days" style="--start:5"><i>1</i><i>2</i><i>3</i><i>4</i><i>5</i><i>6</i><i>7</i><i>8</i><i>9</i><i>10</i><i>11</i><i>12</i><i>13</i><i>14</i><i>15</i><i>16</i><i>17</i><i>18</i><i>19</i><i>20</i><i>21</i><i>22</i><i>23</i><i>24</i><i>25</i><i>26</i><i>27</i><i>28</i><i>29</i><i>30</i><i>31</i></div>
        <p class="month-name">AUG</p>
      </div>
      <div class="month">
        <div class="weekdays"><span>SUN</span><span>MON</span><span>TUE</span><span>WED</span><span>THU</span><span class="weekend">FRI</span><span class="weekend">SAT</span></div>
        <div class="days" style="--start:1"><i>1</i><i>2</i><i>3</i><i>4</i><i>5</i><i>6</i><i>7</i><i>8</i><i>9</i><i>10</i><i>11</i><i>12</i><i>13</i><i>14</i><i>15</i><i>16</i><i>17</i><i>18</i><i>19</i><i>20</i><i>21</i><i>22</i><i>23</i><i>24</i><i>25</i><i>26</i><i>27</i><i>28</i><i>29</i><i>30</i></div>
        <p class="month-name">SEP</p>
      </div>
      <div class="month">
        <div class="weekdays"><span>SUN</span><span>MON</span><span>TUE</span><span>WED</span><span>THU</span><span class="weekend">FRI</span><span class="weekend">SAT</span></div>
        <div class="days" style="--start:3"><i>1</i><i>2</i><i>3</i><i>4</i><i>5</i><i>6</i><i>7</i><i>8</i><i>9</i><i>10</i><i>11</i><i>12</i><i>13</i><i>14</i><i>15</i><i>16</i><i>17</i><i>18</i><i>19</i><i>20</i><i>21</i><i>22</i><i>23</i><i>24</i><i>25</i><i>26</i><i>27</i><i>28</i><i>29</i><i>30</i><i>31</i></div>
        <p class="month-name">OCT</p>
      </div>
      <div class="month">
        <div class="weekdays"><span>SUN</span><span>MON</span><span>TUE</span><span>WED</span><span>THU</span><span class="weekend">FRI</span><span class="weekend">SAT</span></div>
        <div class="days" style="--start:6"><i>1</i><i>2</i><i>3</i><i>4</i><i>5</i><i>6</i><i>7</i><i>8</i><i>9</i><i>10</i><i>11</i><i>12</i><i>13</i><i>14</i><i>15</i><i>16</i><i>17</i><i>18</i><i>19</i><i>20</i><i>21</i><i>22</i><i>23</i><i>24</i><i>25</i><i>26</i><i>27</i><i>28</i><i>29</i><i>30</i></div>
        <p class="month-name">NOV</p>
        <p class="year">2019</p>
      </div>
      <div class="month">
        <div class="weekdays"><span>SUN</span><span>MON</span><span>TUE</span><span>WED</span><span>THU</span><span class="weekend">FRI</span><span class="weekend">SAT</span></div>
        <div class="days" style="--start:1"><i>1</i><i>2</i><i>3</i><i>4</i><i>5</i><i>6</i><i>7</i><i>8</i><i>9</i><i>10</i><i>11</i><i>12</i><i>13</i><i>14</i><i>15</i><i>16</i><i>17</i><i>18</i><i>19</i><i>20</i><i>21</i><i>22</i><i>23</i><i>24</i><i>25</i><i>26</i><i>27</i><i>28</i><i>29</i><i>30</i><i>31</i></div>
        <p class="month-name">DEC</p>
      </div>
    </div>
  </section>
</main>
</body>
</html>
```